Multi-purose Thank You Card Design Project (Real Estate)

We are in the business of listing and selling luxury homes in Atlanta Georgia and are the #1 Award Winning team in our office, #5 in Georgia and #5 in Southeast for all Brandt Halloway team. Your can learn more about us at www.marrowbyandpartners.example.

In our business model, growing a team to $80 million in sales (we will sell $40,000,000 in 2013 and are determined to grow rapidly while providing high levels of service) requires that we carefully nurture our sphere of influence database through multiple, high quality, well-designed touches like (thank you cards, letters, phone calls, gifts etc)

We need a thank you card:
1. Can be used for multiple purposes
a. Referral thank you.
b. House closing anniversary thank you
2. File built in Photoshop with layers that we can edit (we are proficient in Photoshop)
3. Design based on the Brandt Halloway luxury Style Guide but does not restrict your creativity. Break the rules and have more impact.
5. Card 7" w x 5' h opening at top
Updates

The first place payment guarantee has been increased by $100 to $320.

The attached logo files have been replaced and should open correctly.
Kindly,
Pelford

Target Market(s)

Buyers and Seller of Homes from $300k to $10m

Industry/Entity Type

Business

Requirements
Must have
• Copy on cover: "Thanks for the Referral"
Logo 1: Brandt Halloway Luxury Logo
File in 300 dpi for print
File in 96 dpi for use with Post Ahead Notes
Nice to have
• Photo of Home (optional)
Logo 2 Marrowby and Partners Logo (optional)

```html
<!DOCTYPE html>
<html lang="en">
<head>
<meta charset="utf-8">
<title>Thanks for the Referral – Card</title>
<link rel="stylesheet" href="https://fonts.googleapis.com/css2?family=Crimson+Pro:wght@700&family=Open+Sans:wght@300;400&family=Delius&display=swap">
<style>
  :root {
    --page: #ffffff;
    --crimson-core: #d3264a;
    --crimson-mid: #a8213d;
    --crimson-edge: #4a1c24;
    --cream: #fdf8e6;
    --cream-deep: #f6efd3;
    --fold: rgba(255,255,255,0.35);
    --fold-cream: rgba(160,130,80,0.18);
    --orange-light: #f6a23a;
    --orange-deep: #e4741c;
    --white: #ffffff;
    --badge: #2b2a2a;
    --badge-text: #f1f1f1;
    --gold: #c9a463;
    --gold-light: #e7cd97;
    --brown: #5c3a26;
    --parchment: #efdfb2;
    --parchment-dark: #c9a866;
    --ink: #4b2e1e;
  }
  * { margin: 0; padding: 0; box-sizing: border-box; }
  html, body { width: 1200px; height: 835px; overflow: hidden; background: var(--page); }
  .card-spread { position: relative; width: 1200px; height: 835px; }

  .panel { position: absolute; top: 0; width: 583px; height: 835px; overflow: hidden; }
  .panel--cover {
    left: 0;
    background: radial-gradient(ellipse 70% 60% at 50% 50%, var(--crimson-core) 0%, var(--crimson-mid) 55%, var(--crimson-edge) 100%);
  }
  .panel--inside {
    left: 617px;
    background: radial-gradient(ellipse 80% 60% at 50% 50%, #fffdf2 0%, var(--cream) 60%, var(--cream-deep) 100%);
  }
  .fold-line { position: absolute; left: 0; top: 417px; width: 100%; height: 1px; background: var(--fold); }
  .panel--inside .fold-line { background: var(--fold-cream); }

  .brand-badge {
    position: absolute; left: 170px; top: 168px; width: 245px; height: 82px;
    background: var(--badge);
    transform: rotate(180deg);
    display: flex; align-items: center; justify-content: center; gap: 12px;
  }
  .brand-badge__mark { width: 14px; height: 14px; background: var(--badge-text); }
  .brand-badge__name {
    font-family: "Open Sans", sans-serif; font-weight: 400;
    font-size: 14px; letter-spacing: 2px; line-height: 1.35;
    color: var(--badge-text); text-transform: uppercase;
  }

  .cover-title { position: absolute; left: 0; top: 0; width: 100%; height: 100%; }
  .cover-title__main {
    position: absolute;
    font-family: "Crimson Pro", serif; font-weight: 700;
    color: var(--orange-deep);
    background: linear-gradient(180deg, var(--orange-light), var(--orange-deep));
    -webkit-background-clip: text; background-clip: text; -webkit-text-fill-color: transparent;
    letter-spacing: -1px; line-height: 1;
  }
  .cover-title__thanks { left: 122px; top: 518px; font-size: 66px; }
  .cover-title__referral { left: 247px; top: 572px; font-size: 64px; }
  .cover-title__connector {
    position: absolute; left: 328px; top: 541px;
    font-family: "Open Sans", sans-serif; font-weight: 300;
    font-size: 33px; color: var(--white); line-height: 1;
  }

  .house-row { position: absolute; }
  .house-row--cover {
    left: 0; top: 705px; width: 583px; height: 130px;
    background: linear-gradient(180deg, rgba(201,164,99,0) 0%, rgba(201,164,99,0.35) 45%, rgba(92,58,38,0.55) 100%);
  }
  .house-row--inside {
    left: 0; top: 140px; width: 583px; height: 140px;
    background: linear-gradient(90deg, rgba(92,58,38,0.35), rgba(201,164,99,0.35) 45%, rgba(231,205,151,0.3));
  }

  .scroll-art {
    position: absolute; left: 108px; top: 450px; width: 360px; height: 362px;
    background: linear-gradient(135deg, var(--parchment) 0%, #f7ebc6 45%, var(--parchment-dark) 100%);
    border-radius: 14px;
  }
  .scroll-message {
    position: absolute; left: 140px; top: 475px; width: 230px;
    font-family: "Delius", cursive; font-size: 11.5px; line-height: 16.6px;
    color: var(--ink); text-align: center;
  }
  .scroll-message p + p { margin-top: 0; }
  .scroll-signoff {
    position: absolute; left: 209px; top: 682px;
    font-family: "Delius", cursive; font-size: 15px; color: var(--ink);
  }
</style>
</head>
<body>
<main class="card-spread">
  <section class="panel panel--cover">
    <div class="brand-badge">
      <span class="brand-badge__mark"></span>
      <span class="brand-badge__name">Luxury Homes<br>Brandt Halloway</span>
    </div>
    <div class="fold-line"></div>
    <h1 class="cover-title">
      <span class="cover-title__main cover-title__thanks">Thanks</span>
      <span class="cover-title__connector">for the</span>
      <span class="cover-title__main cover-title__referral">referral</span>
    </h1>
    <div class="house-row house-row--cover" role="img" aria-label="Row of gold and brown house outline rooftops"></div>
  </section>

  <section class="panel panel--inside">
    <div class="house-row house-row--inside" role="img" aria-label="Row of gold and brown house outline rooftops"></div>
    <div class="fold-line"></div>
    <div class="scroll-art" role="img" aria-label="Unrolled parchment scroll with a golden quill pen and ink splash"></div>
    <div class="scroll-message">
      <p>Lorem ipsum dolor sit amet, consectetuer adipiscing elit. Nam cursus. Morbi ut mi. Nullam enim leo, egestas id, condimentum at, laoreet mattis, massa.</p>
      <p>Sed eleifend nonummy diam. Praesent mauris ante, elementum et, bibendum at, posuere sit amet, nibh. Duis tincidunt lectus quis dui viverra vestibulum.</p>
    </div>
    <p class="scroll-signoff">Thank You !</p>
  </section>
</main>
</body>
</html>
```